【画像サイズ】※MZSより抜粋
表紙ファイルの理想的な採寸は2,560×1,600ピクセルです。
注:画像の寸法は1,000×625ピクセル以上であることが必要です。
画像の最大の寸法は10,000×10,000ピクセルです。

【タイトル】
家族向け専任相談員がすすめる日々の工夫
ドキドキ平気!まあるい毎日の育ち術

サブキャッチ
心理学×四柱推命メソッド
我が子を上手に愛したいあなたへ

【著者】
ひだまりファミリーケア協会 もりした かなえ

【本の内容】
子どもを怒って、自分を責めてしまうお母様向けです。
子育ての悩みを、育児書やインターネット情報では効果がなかったり
どちらにも相談できなかったりする現状。
心理学×四柱推命メソッドで、お母様とお子様だけの簡単な解決方法を
やさしくお伝えします。
子どもと過ごすのが楽しくなり、母子ともに満たされ笑顔・Happyな暮らしを実現します。

※本文を参考資料として添付いたします。

【デザイン要望】
タイトル、サブキャッチと合わせて
読者様特典プレゼントのアピールもしたいです。

読者様特典として、イラストでやさしくわかりやすい!四柱推命電子書籍プレゼント

特にイメージにこだわりはありませんので、
自由な発想でのデザインご応募を楽しみにしております。

※次点、次々点の方への参加報酬を設定いたしました。

※その他、必要な情報がありましたら、お問い合わせください。
どうぞ、よろしくお願いいたします。

依頼のジャンルは、子育て・母親向け・育児法・心理学・学び・カウンセリング です。
カテゴリーに近いものがなく、ひとまず、資格・習い事としております。

優しい色使いと、見やすいタイトル、まとまり感でこちらに決定いたしました。

たくさんの素晴らしい商品にに感動しました。本当にありがとうございました。どちらも選びたくて本当に、迷いに迷いました。

```html
<!DOCTYPE html>
<html lang="ja">
<head>
<meta charset="utf-8">
<title>ドキドキ平気!まあるい毎日の育ち術</title>
<link href="https://fonts.googleapis.com/css2?family=M+PLUS+Rounded+1c:wght@500;800&family=Shippori+Mincho:wght@700&family=Yusei+Magic&display=swap" rel="stylesheet">
<style>
:root{
  --pink:#ef4a93;
  --yellow:#fff36a;
  --white:#ffffff;
  --gray:#8a8a8a;
  --photo-a:#f6d9e3;
  --photo-b:#e9b7c8;
  --photo-c:#c98ea5;
}
*{margin:0;padding:0;box-sizing:border-box}
html,body{width:750px;height:1200px;overflow:hidden;background:var(--white)}
.cover{position:relative;width:750px;height:1200px;overflow:hidden;font-family:"M PLUS Rounded 1c",sans-serif}
.cover-photo{position:absolute;inset:0;background:
  radial-gradient(ellipse at 40% 45%,var(--photo-a) 0%,var(--photo-b) 45%,var(--photo-c) 100%)}
.abs{position:absolute;white-space:nowrap}
.outlined{paint-order:stroke fill}
.headline-band{left:0;top:0;width:720px;height:88px;background:rgba(255,255,255,.92)}
.headline{left:14px;top:2px;font-size:72px;font-weight:800;color:var(--pink);line-height:1.15;letter-spacing:4px}
.info-band{left:0;top:90px;width:750px;height:78px;background:rgba(255,255,255,.85)}
.org{left:12px;top:94px;font-size:28px;font-weight:500;color:var(--gray);line-height:1.3}
.author{left:312px;top:104px;font-size:40px;font-weight:800;color:var(--pink);line-height:1.2}
.lead{font-weight:800;color:var(--yellow);-webkit-text-stroke:6px var(--pink);line-height:1;left:0;width:750px;text-align:center}
.lead-1{top:176px;font-size:44px}
.lead-2{top:224px;font-size:36px}
.title-band{left:0;top:266px;width:750px;height:76px;background:var(--pink)}
.title{left:0;width:750px;text-align:center;top:272px;font-size:60px;font-weight:800;color:var(--white);line-height:1.1}
.bubble{left:510px;top:360px;width:240px;height:250px}
.bubble-text{left:560px;top:420px;font-family:"Yusei Magic",sans-serif;font-size:40px;color:var(--pink);line-height:1.25;transform:rotate(18deg);text-align:center}
.perk{font-size:44px;font-weight:800;line-height:1;-webkit-text-stroke:6px var(--pink)}
.perk-psych{left:12px;top:656px;font-size:42px;color:var(--white);font-family:"Shippori Mincho",serif}
.perk-illust{left:200px;top:656px;color:var(--yellow)}
.perk-book{left:280px;top:712px;color:var(--yellow)}
.perk-gift{left:300px;top:768px;color:var(--yellow)}
.message{left:170px;top:812px;font-family:"Yusei Magic",sans-serif;font-size:30px;color:var(--pink);-webkit-text-stroke:5px var(--white);transform:rotate(10deg);transform-origin:left top}
.method{right:14px;top:1136px;font-family:"Shippori Mincho",serif;font-weight:700;font-size:44px;color:var(--white);-webkit-text-stroke:6px var(--pink);line-height:1}
</style>
</head>
<body>
<div class="cover">
  <div class="cover-photo" role="img" aria-label="ピンク色の毛布にくるまって眠る赤ちゃんの写真"></div>

  <div class="abs headline-band"></div>
  <h1 class="abs headline">ドキドキも平気!</h1>

  <div class="abs info-band"></div>
  <p class="abs org">ひだまりファミリー<br>ケア協会</p>
  <p class="abs author">著：もりした かなえ</p>

  <p class="abs lead lead-1 outlined">家族向け専任相談員がすすめる</p>
  <p class="abs lead lead-2 outlined">日々の工夫</p>

  <div class="abs title-band"></div>
  <h2 class="abs title">まあるい毎日の育ち術</h2>

  <svg class="abs bubble" viewBox="0 0 240 250" aria-hidden="true">
    <path d="M140 20 A98 98 0 1 1 62 185 L0 215 L48 158 A98 98 0 0 1 140 20 Z" fill="#ffffff"/>
  </svg>
  <p class="abs bubble-text">特典が<br>あるよ</p>

  <p class="abs perk perk-psych outlined">心理学</p>
  <p class="abs perk perk-illust outlined">わかりやすいイラスト付</p>
  <p class="abs perk perk-book outlined">四柱推命電子書籍</p>
  <p class="abs perk perk-gift outlined">プレゼント!!</p>

  <p class="abs message outlined">我が子を上手に愛したいあなたへ</p>

  <p class="abs method outlined">四柱推命メソッド</p>
</div>
</body>
</html>
```